Brochure & Business card design

Looking for a new business card design i want it to be modern and sharp looking i usually order plastic business cards, and i would like to make the colors like the logo teal/charcoal i will like to have our services on icons with words.... our services are
ROOFING GUTTERS PAINTING PRESSURE WASHING EXTERIOR DESIGN & ATTIC VENTILATION. I also want to add my credentials

Target Market(s)

Oregon local market

Industry/Entity Type

Residential Construction

Contact Information for Business Card

Business info, services, number, website

Font styles to use
Serif
Sans Serif

Colors
33b8a4
5c5c5c
ffffff

Requirements
Must have
• Dale Finch
• Cell:
• Office:
• Email:
• Website:
• also i need our social media icons
• Services ROOFING GUTTERS PAINTING PRESSURE WASHING EXTERIOR DESIGN & ATTIC VENTILATION
• -icons for number, web, email, cell
• OR #584312
• Wa #KTRABLD461X7
Nice to have
• -Clean design Front & Back
• -Icons
• -shape House just like logo design
• -First Impression
Should not have
• Not Busy or lost of eye contact

```html
<!DOCTYPE html>
<html lang="en">
<head>
<meta charset="utf-8">
<title>Ridgeline Exteriors – Business Card</title>
<link href="https://fonts.googleapis.com/css2?family=Arimo:wght@400;700&display=swap" rel="stylesheet">
<style>
  :root {
    --teal: #33b8a4;
    --teal-deep: #1f8f80;
    --charcoal: #5c5c5c;
    --ink: #1e1e1e;
    --paper: #ffffff;
    --stage: #2b2b2b;
    --muted: #8a8a8a;
  }
  * { margin: 0; padding: 0; box-sizing: border-box; }
  html, body { width: 1200px; height: 997px; overflow: hidden; }
  body {
    background: var(--stage);
    font-family: "Arimo", Arial, sans-serif;
    position: relative;
  }
  .card {
    position: absolute;
    top: 340px;
    width: 540px;
    height: 310px;
    background: var(--paper);
    overflow: hidden;
  }
  .card--back { left: 40px; }
  .card--front { left: 620px; }

  /* Brand name stand-in */
  .brand {
    position: absolute;
    display: flex;
    align-items: center;
    gap: 10px;
    color: var(--teal);
    font-weight: 700;
    letter-spacing: 1px;
    text-transform: uppercase;
  }
  .brand__square { background: var(--teal); display: block; }
  .card--back .brand { left: 60px; top: 170px; font-size: 24px; }
  .card--back .brand__square { width: 22px; height: 22px; }
  .card--front .brand { left: 175px; top: 62px; font-size: 20px; }
  .card--front .brand__square { width: 18px; height: 18px; }

  /* Services list */
  .services {
    position: absolute;
    right: 40px;
    top: 38px;
    list-style: none;
    text-align: right;
  }
  .services__item {
    font-size: 10px;
    font-weight: 700;
    color: var(--muted);
    letter-spacing: 1px;
    line-height: 22px;
    display: flex;
    justify-content: flex-end;
    align-items: center;
    gap: 8px;
  }
  .services__item::after {
    content: "";
    width: 6px; height: 6px;
    border-radius: 50%;
    background: var(--teal);
  }

  /* Credential badges */
  .badges { position: absolute; left: 60px; top: 232px; display: flex; gap: 12px; }
  .badge { height: 22px; border-radius: 3px; }
  .badge--certified { width: 58px; background: #c9302c; }
  .badge--accredited { width: 34px; background: var(--ink); }

  /* Front card */
  .rule { position: absolute; height: 1px; background: var(--ink); }
  .rule--brand { left: 430px; right: 0; top: 118px; }
  .rule--name { left: 170px; width: 240px; top: 165px; }

  .person { position: absolute; left: 30px; top: 155px; }
  .person__name { font-size: 15px; font-weight: 700; color: var(--teal-deep); letter-spacing: .5px; text-transform: uppercase; }
  .person__role { font-size: 11px; color: var(--ink); margin-top: 1px; }

  .contacts { position: absolute; left: 30px; top: 208px; list-style: none; }
  .contacts__item { display: flex; align-items: center; gap: 12px; font-size: 12px; color: var(--ink); height: 20px; letter-spacing: .3px; }
  .contacts__icon { width: 14px; height: 14px; }

  .address {
    position: absolute; right: 28px; top: 188px;
    text-align: right; font-size: 11px; color: var(--teal-deep); line-height: 15px;
  }
  .footer-band { position: absolute; left: 0; bottom: 0; }
  .website {
    position: absolute; right: 28px; bottom: 26px;
    font-size: 12px; font-weight: 700; color: var(--paper); letter-spacing: 1.5px;
  }
</style>
</head>
<body>

<section class="card card--back" aria-label="Card back">
  <ul class="services">
    <li class="services__item">ROOFING</li>
    <li class="services__item">GUTTERS</li>
    <li class="services__item">PAINTING</li>
    <li class="services__item">EXTERIOR DESIGN</li>
    <li class="services__item">ATTIC VENTILATION</li>
    <li class="services__item">PRESSURE WASHING</li>
  </ul>
  <div class="brand"><span class="brand__square"></span>Ridgeline Exteriors</div>
  <div class="badges">
    <span class="badge badge--certified" role="img" aria-label="Certification badge"></span>
    <span class="badge badge--accredited" role="img" aria-label="Accreditation badge"></span>
  </div>
</section>

<section class="card card--front" aria-label="Card front">
  <div class="brand"><span class="brand__square"></span>Ridgeline Exteriors</div>
  <span class="rule rule--brand"></span>

  <div class="person">
    <p class="person__name">Owen Hartley</p>
    <p class="person__role">General Manager</p>
  </div>
  <span class="rule rule--name"></span>

  <ul class="contacts">
    <li class="contacts__item">
      <svg class="contacts__icon" viewBox="0 0 14 14"><circle cx="7" cy="7" r="7" fill="#33b8a4"/><path d="M4 5.5c0-1 1-1.5 3-1.5s3 .5 3 1.5M5 6.5h4l.8 3.5H4.2z" fill="none" stroke="#fff" stroke-width="1"/></svg>
      0161 482 5917
    </li>
    <li class="contacts__item">
      <svg class="contacts__icon" viewBox="0 0 14 14"><circle cx="7" cy="7" r="7" fill="#33b8a4"/><rect x="5" y="3.5" width="4" height="7" rx=".8" fill="none" stroke="#fff" stroke-width="1"/></svg>
      07521 604 838
    </li>
    <li class="contacts__item">
      <svg class="contacts__icon" viewBox="0 0 14 14"><circle cx="7" cy="7" r="7" fill="#33b8a4"/><rect x="3.8" y="4.8" width="6.4" height="4.6" fill="none" stroke="#fff" stroke-width="1"/><path d="M3.8 4.8L7 7.4l3.2-2.6" fill="none" stroke="#fff" stroke-width="1"/></svg>
      ohartley@ridgeline-works.co.uk
    </li>
  </ul>

  <p class="address">Carrow Lane Denford<br>Leeds LS9 4QT</p>

  <svg class="footer-band" width="540" height="80" viewBox="0 0 540 80">
    <path d="M0 70 H290 C310 70 310 26 336 26 H540" fill="none" stroke="#1e1e1e" stroke-width="6"/>
    <path d="M0 76 H300 C318 76 320 34 344 34 H540 V80 H0 Z" fill="#33b8a4"/>
  </svg>
  <p class="website">www.ridgeline-works.com</p>
</section>

</body>
</html>
```